Logo redesign & Stationery Design Project

We need a logo redesign for our company.

We also require the following stationary with the new logo:
*letterhead
*With compliments slips
*business card
*envelopes

We would like to maintain our current colours of navy blue and gold. We would like to maintain the wording on the back of our current business card.

Our existing letterhead and business card is attached.

Target Market(s)

Medical Professionals, Pharmacists, Lawyers

Industry/Entity Type

Business

Requirements
Must have
• See attached business card and letterhead, as all details on these documents need to be included.

```html
<!DOCTYPE html>
<html lang="en">
<head>
<meta charset="utf-8">
<title>Halden Marsh Financial Services – Stationery</title>
<link href="https://fonts.googleapis.com/css2?family=Michroma&display=swap" rel="stylesheet">
<style>
  :root {
    --navy: #2b2773;
    --navy-deep: #26216a;
    --gold: #c9962e;
    --gold-light: #f3d86a;
    --paper: #ffffff;
    --backdrop: #e6e4e0;
    --muted-navy: #4a4690;
  }
  * { box-sizing: border-box; margin: 0; padding: 0; }
  html, body {
    width: 1200px; height: 849px; overflow: hidden;
    background: var(--backdrop);
    font-family: "Michroma", "Arial", sans-serif;
    color: var(--navy);
  }
  .stage { position: relative; width: 1200px; height: 849px; }

  .gold-band {
    position: absolute; left: 0; right: 0; bottom: 0;
    background: linear-gradient(90deg, #a8741f 0%, var(--gold) 20%, var(--gold-light) 50%, var(--gold) 80%, #a8741f 100%);
  }

  /* Letterhead */
  .letterhead {
    position: absolute; left: 124px; top: 40px; width: 595px; height: 770px;
    background: var(--paper);
    box-shadow: 0 2px 6px rgba(0,0,0,.18);
  }
  .letterhead .gold-band { height: 12px; }
  .brand-mark {
    display: flex; align-items: center; justify-content: center; gap: 8px;
    color: var(--navy); font-size: 15px; letter-spacing: 1px;
  }
  .brand-mark .square { width: 14px; height: 14px; background: var(--navy); }
  .letterhead .brand-mark { position: absolute; top: 88px; left: 0; right: 0; }
  .letterhead .company-name {
    position: absolute; top: 114px; left: 0; right: 0; text-align: center;
    font-size: 12.5px; letter-spacing: .6px;
  }
  .letterhead .abn {
    position: absolute; top: 130px; left: 0; right: 0; text-align: center;
    font-size: 10.5px; letter-spacing: .5px;
  }
  .letterhead-footer {
    position: absolute; left: 0; right: 0; top: 706px; text-align: center;
    font-size: 7px; letter-spacing: .4px; line-height: 12px; text-transform: uppercase;
  }
  .letterhead-footer .label, .letterhead-footer .web { color: var(--gold); }
  .letterhead-footer .rep { margin-top: 8px; }

  /* Business cards */
  .card {
    position: absolute; top: 268px; width: 140px; height: 245px;
    box-shadow: 0 2px 5px rgba(0,0,0,.2);
    overflow: hidden; background: var(--navy-deep);
  }
  .card .gold-band { height: 10px; }
  .card-front { left: 768px; }
  .card-back { left: 937px; }

  .card-front .card-head {
    position: absolute; top: 0; left: 0; right: 0; height: 102px; background: var(--paper);
  }
  .card-front .brand-mark { position: absolute; top: 35px; left: 0; right: 0; font-size: 9px; gap: 5px; }
  .card-front .brand-mark .square { width: 9px; height: 9px; }
  .card-front .company-name {
    position: absolute; top: 70px; left: 0; right: 0; text-align: center;
    font-size: 6.6px; line-height: 9px; letter-spacing: .2px;
  }
  .card-front .person {
    position: absolute; top: 136px; left: 0; right: 0; text-align: center; color: #fff;
    font-size: 5.6px; line-height: 8px; letter-spacing: .3px;
  }
  .card-front .person .role { font-size: 4.6px; }
  .card-front .contact {
    position: absolute; top: 184px; left: 6px; right: 6px; text-align: center; color: #fff;
    font-size: 4.3px; line-height: 8.2px; text-transform: uppercase;
  }
  .card-front .contact .label, .card-front .contact .web { color: var(--gold); }

  .value {
    position: absolute; left: 0; right: 0; text-align: center;
  }
  .value .word { color: var(--gold); font-size: 11px; letter-spacing: 1.6px; line-height: 12px; }
  .value .desc { color: #fff; font-size: 4.2px; letter-spacing: .2px; }
  .value-1 { top: 34px; }
  .value-2 { top: 64px; }
  .value-3 { top: 94px; }

  .card-back .faint-mark {
    position: absolute; top: 138px; left: 0; right: 0;
    display: flex; justify-content: center;
  }
  .card-back .faint-mark .square { width: 30px; height: 30px; border: 1.5px solid var(--muted-navy); }
  .card-back .faint-name {
    position: absolute; top: 176px; left: 0; right: 0; text-align: center;
    color: var(--muted-navy); font-size: 6px; line-height: 8px;
  }
  .card-back .representative {
    position: absolute; top: 204px; left: 4px; right: 4px; text-align: center; color: #fff;
    font-size: 4px; line-height: 6px; text-transform: uppercase;
  }
</style>
</head>
<body>
<main class="stage">

  <section class="letterhead" aria-label="Letterhead">
    <div class="brand-mark"><span class="square"></span><span>HALDEN MARSH</span></div>
    <h1 class="company-name">HALDEN MARSH FINANCIAL SERVICES</h1>
    <p class="abn">ABN 51 302 846 117</p>

    <footer class="letterhead-footer">
      <p>Suite 4, 112-118 Harbour Road. Kirrawee NSW 2232 | PO Box 4820 Kirrawee NSW 2232</p>
      <p><span class="label">T</span> 02 9000 4410 | <span class="label">F</span> 02 9000 4413 | <span class="label">E</span> admin@haldenmarsh.com.au | <span class="web">www.haldenmarsh.com.au</span></p>
      <p class="rep">Corporate authorised representative of Meridian Advisory Group AFSL 408215</p>
    </footer>
    <div class="gold-band"></div>
  </section>

  <section class="card card-front" aria-label="Business card front">
    <div class="card-head">
      <div class="brand-mark"><span class="square"></span><span>HALDEN MARSH</span></div>
      <h2 class="company-name">HALDEN MARSH<br>FINANCIAL SERVICES</h2>
    </div>
    <div class="person">
      <p>DANIEL (DAN) HALDEN</p>
      <p class="role">PARTNER</p>
    </div>
    <div class="contact">
      <p>Suite 4, 112-118 Harbour Road.</p>
      <p>Kirrawee NSW 2232</p>
      <p><span class="label">T</span> 02 9000 4410 | <span class="label">M</span> 0400 000 318</p>
      <p><span class="label">E</span> admin@haldenmarsh.com.au</p>
      <p class="web">www.haldenmarsh.com.au</p>
    </div>
    <div class="gold-band"></div>
  </section>

  <section class="card card-back" aria-label="Business card back">
    <div class="value value-1"><p class="word">CERTAINTY</p><p class="desc">DESIGNING INSURANCE SOLUTIONS</p></div>
    <div class="value value-2"><p class="word">CLARITY</p><p class="desc">STRATEGIC PLANNING ADVICE</p></div>
    <div class="value value-3"><p class="word">CONFIDENCE</p><p class="desc">CONSTRUCTING RETIREMENT PLANS</p></div>
    <div class="faint-mark"><span class="square"></span></div>
    <p class="faint-name">HALDEN MARSH<br>FINANCIAL SERVICES</p>
    <p class="representative">Corporate authorised representative<br>of Meridian Advisory Group<br>AFSL 408215</p>
    <div class="gold-band"></div>
  </section>

</main>
</body>
</html>
```